Präsentationsvorlagen / Powerpoint Master for my company
Zielgruppe
Offline hardware device to manage and save passwords safely.
Aufgabenstellung
DIN A4 quer

```html
<!DOCTYPE html>
<html lang="en">
<head>
<meta charset="utf-8">
<title>Lockwell Presentation Template – Content Slide</title>
<link rel="stylesheet" href="https://fonts.googleapis.com/css2?family=Montserrat:wght@400;700&family=Source+Sans+3:wght@400&display=swap">
<style>
  :root {
    --page-bg: #f2f2f2;
    --slide-bg: #ffffff;
    --brand-green: #2b7a3b;
    --ink: #141414;
    --footer-black: #151515;
    --white: #ffffff;
    --photo-light: #d9d6cf;
    --photo-dark: #3a3a38;
  }
  * { margin: 0; padding: 0; box-sizing: border-box; }
  html, body {
    width: 882px;
    height: 1200px;
    overflow: hidden;
    background: var(--page-bg);
  }
  .canvas {
    position: relative;
    width: 882px;
    height: 1200px;
  }
  .slide {
    position: absolute;
    left: 41px;
    top: 317px;
    width: 800px;
    height: 566px;
    background: var(--slide-bg);
    box-shadow: 3px 3px 6px rgba(0,0,0,0.25);
    overflow: hidden;
    color: var(--ink);
  }
  .slide-header {
    position: absolute;
    left: 43px;
    top: 44px;
    font-family: "Montserrat", sans-serif;
    font-weight: 700;
    font-size: 23px;
    line-height: 1;
    color: var(--ink);
  }
  .slide-header .accent { color: var(--brand-green); }
  .brand-name {
    position: absolute;
    right: 40px;
    top: 36px;
    display: flex;
    align-items: center;
    gap: 8px;
    font-family: "Montserrat", sans-serif;
    font-weight: 700;
    font-size: 30px;
    line-height: 1;
    color: var(--ink);
  }
  .brand-name .brand-mark {
    width: 14px;
    height: 14px;
    background: var(--brand-green);
  }
  .photo {
    position: absolute;
    left: 0;
    top: 106px;
    width: 322px;
    height: 355px;
    background: linear-gradient(135deg, var(--photo-light) 0%, #a9a59b 45%, var(--photo-dark) 100%);
  }
  .photo-corner {
    position: absolute;
    left: 0;
    top: 0;
    width: 800px;
    height: 566px;
    pointer-events: none;
  }
  .content {
    position: absolute;
    left: 358px;
    top: 110px;
    width: 390px;
  }
  .content-title {
    font-family: "Montserrat", sans-serif;
    font-size: 37px;
    line-height: 1.2;
    margin-bottom: 20px;
  }
  .content-title .light { display: block; font-weight: 400; color: var(--ink); }
  .content-title .bold { display: block; font-weight: 700; color: var(--brand-green); }
  .content p {
    font-family: "Source Sans 3", sans-serif;
    font-size: 10.6px;
    line-height: 18px;
    color: var(--ink);
    margin-bottom: 11px;
  }
  .slide-footer {
    position: absolute;
    left: 0;
    bottom: 0;
    width: 800px;
    height: 30px;
    background: var(--footer-black);
  }
  .footer-title {
    position: absolute;
    left: 40px;
    top: 8px;
    font-family: "Montserrat", sans-serif;
    font-weight: 700;
    font-size: 12px;
    color: var(--white);
  }
  .page-tab {
    position: absolute;
    right: 0;
    bottom: 0;
    width: 107px;
    height: 40px;
    background: var(--brand-green);
    border-top-left-radius: 24px;
    display: flex;
    align-items: center;
    justify-content: center;
    font-family: "Montserrat", sans-serif;
    font-weight: 700;
    font-size: 17px;
    color: var(--white);
  }
</style>
</head>
<body>
<div class="canvas">
  <section class="slide">
    <h2 class="slide-header"><span class="accent">Header</span> Goes Here</h2>
    <div class="brand-name"><span class="brand-mark"></span>Lockwell</div>

    <div class="photo" role="img" aria-label="Photo of a hand lifting the receiver of a desk telephone, plant in the background"></div>
    <svg class="photo-corner" viewBox="0 0 800 566" aria-hidden="true">
      <polygon points="331,401 331,473 242,473" fill="#2b7a3b"/>
    </svg>

    <div class="content">
      <h3 class="content-title">
        <span class="light">Lorem</span>
        <span class="bold">Ipsum Dolor</span>
      </h3>
      <p>Lorem ipsum dolor sit amet, consectetur adipiscing elit, sed do eiusmod tempor incididunt ut labore et dolore magna aliqua. Ut enim ad minim veniam, quis nostrud exercitation ullamco laboris nisi ut aliquip ex ea commodo consequat. Duis aute irure dolor in reprehenderit in voluptate velit esse cillum dolore eu fugiat nulla pariatur. Excepteur sint occaecat cupidatat non proident, sunt in culpa qui officia deserunt mollit anim id est laborum.</p>
      <p>Lorem ipsum dolor sit amet, consectetur adipiscing elit, sed do eiusmod tempor incididunt ut labore et dolore magna aliqua. Ut enim ad minim veniam, quis nostrud exercitation ullamco laboris nisi ut aliquip ex ea commodo consequat. Duis aute irure dolor in reprehenderit in voluptate velit esse cillum dolore eu fugiat nulla pariatur. Excepteur sint occaecat cupidatat non proident, sunt in culpa qui officia deserunt mollit anim id est laborum.</p>
    </div>

    <footer class="slide-footer">
      <span class="footer-title">lockwell Presentation Title 2023</span>
    </footer>
    <div class="page-tab">03</div>
  </section>
</div>
</body>
</html>
```